Business Card design for an International Import Export House

We need a Business Card design for our import export business. We trade in Minerals, Metals, Rice, Sugar, Steel etc.. The design should be minimalistic. It may or may not contain the physical address. In case you want to include the physical address - 418 Verandah Heights, Marlow Sector 9, Lindell, Korvana, India, 560417.

Target Market(s)

Steel Mills or Steel Plants, Factories, Mining businesses, Industrial houses, Government Agencies

Industry/Entity Type

Importer

Contact Information for Business Card

Business Name - Tessan Overseas

Font styles to use
Other font styles liked:
• montserrat

Requirements
Must have
• Ravi Kandola - President
• www.tessanoverseas.com
• ravi@tessanoverseas.com
• +91-987-654-3217
Nice to have
• worldwide suppliers of ores

```html
<!DOCTYPE html>
<html lang="en">
<head>
<meta charset="utf-8">
<title>Tessan Overseas – Business Card</title>
<link href="https://fonts.googleapis.com/css2?family=Lato:wght@400;700&display=swap" rel="stylesheet">
<style>
  :root{
    --bg:#d9d9d9;
    --card:#262626;
    --row:#333333;
    --teal:#3f8ea6;
    --paper:#f1f1ef;
    --ink:#1c1c1c;
    --light:#f0f0f0;
  }
  *{box-sizing:border-box;margin:0;padding:0}
  html,body{width:1200px;height:899px;overflow:hidden}
  body{
    background:var(--bg);
    font-family:'Lato',sans-serif;
    display:flex;flex-direction:column;align-items:center;justify-content:center;gap:36px;
  }
  .card{width:700px;height:400px;background:var(--card);position:relative;overflow:hidden;
    box-shadow:0 6px 18px rgba(0,0,0,.18)}
  .brand-tile{position:absolute;background:var(--paper);display:flex;flex-direction:column;
    align-items:center;justify-content:center;gap:22px}
  .front .brand-tile{left:200px;top:60px;width:300px;height:280px}
  .brand-mark{width:70px;height:70px;border-radius:50%;background:var(--teal)}
  .brand-name{font-weight:700;color:var(--teal);font-size:26px;letter-spacing:.5px;text-transform:uppercase}
  .back .accent-bar{position:absolute;left:14px;top:62px;width:46px;height:268px;background:var(--teal)}
  .back .brand-tile{left:66px;top:40px;width:322px;height:298px;border-right:10px solid var(--teal)}
  .contact-list{position:absolute;left:400px;top:28px;right:0;display:flex;flex-direction:column;gap:6px}
  .contact-row{background:var(--row);border-left:8px solid var(--teal);height:64px;
    display:flex;align-items:center;gap:16px;padding-left:16px;color:var(--light)}
  .contact-row.tall{height:80px}
  .contact-row svg{width:18px;height:18px;flex:none;fill:var(--light)}
  .contact-text{font-size:14px;line-height:1.3}
  .person-name{font-size:20px;letter-spacing:.3px}
  .person-name b{font-weight:700}
  .person-role{font-size:12px}
</style>
</head>
<body>
  <section class="card front">
    <div class="brand-tile">
      <span class="brand-mark"></span>
      <span class="brand-name">Tessan Overseas</span>
    </div>
  </section>

  <section class="card back">
    <div class="accent-bar"></div>
    <div class="brand-tile">
      <span class="brand-mark"></span>
      <span class="brand-name">Tessan Overseas</span>
    </div>
    <div class="contact-list">
      <div class="contact-row">
        <svg viewBox="0 0 20 20"><circle cx="10" cy="6" r="4"/><path d="M2 19c0-5 4-7 8-7s8 2 8 7z"/></svg>
        <div class="contact-text">
          <div class="person-name"><b>RAVI</b> KANDOLA</div>
          <div class="person-role">President</div>
        </div>
      </div>
      <div class="contact-row">
        <svg viewBox="0 0 20 20"><circle cx="10" cy="10" r="8.5" fill="none" stroke="#f0f0f0" stroke-width="1.6"/><path d="M7 5.5l2 2-1 1.5c.7 1.4 1.6 2.3 3 3l1.5-1 2 2-1.5 1.5C9.5 14 6 10.5 5.5 7z"/></svg>
        <div class="contact-text">+91-987-654-3217</div>
      </div>
      <div class="contact-row">
        <svg viewBox="0 0 20 20" fill="none" stroke="#f0f0f0" stroke-width="1.5"><circle cx="10" cy="10" r="8.5" fill="none"/><ellipse cx="10" cy="10" rx="3.5" ry="8.5" fill="none"/><path d="M1.5 10h17M3 5.5h14M3 14.5h14"/></svg>
        <div class="contact-text">www.tessanoverseas.com<br>ravi@tessanoverseas.com</div>
      </div>
      <div class="contact-row tall">
        <svg viewBox="0 0 20 20"><path d="M10 2l9 8h-3v8h-4v-5H8v5H4v-8H1z"/></svg>
        <div class="contact-text">418 Verandah Heights,<br>Marlow Sector 9, Lindell,<br>Korvana, India, 560417</div>
      </div>
    </div>
  </section>
</body>
</html>
```